Wordpress Design for a Private Label BBQ Brand

For our new brand, we'd need a new Wordpress website. We'd prefer to run the website on Wordpress

We'd like to include the following
- space for description of the brand
- space for product portfolio (not a shop!)
- space for socials
- space for support
- space for contact

```html
<!DOCTYPE html>
<html lang="en">
<head>
<meta charset="utf-8">
<title>Fiorenzo – Grill to Suit Your Needs</title>
<link href="https://fonts.googleapis.com/css2?family=Libre+Baskerville:wght@700&family=Lato:wght@400;700;900&display=swap" rel="stylesheet">
<style>
:root{
  --ember:#d42f1e;
  --ember-2:#e9592a;
  --ink:#2f2f2f;
  --muted:#555;
  --soft:#f3f3f3;
  --sand:#ead8bc;
  --sand-text:#9b6b3f;
  --night:#231a17;
  --night-2:#1a1210;
  --white:#fff;
}
*{margin:0;padding:0;box-sizing:border-box}
html,body{width:1200px;height:4167px;overflow:hidden}
body{position:relative;font-family:"Lato",sans-serif;color:var(--ink);background:var(--white)}
.abs{position:absolute}
.serif{font-family:"Libre Baskerville",serif}
.btn{position:absolute;display:flex;align-items:center;justify-content:center;gap:8px;background:linear-gradient(90deg,var(--ember),var(--ember-2));color:#fff;font-weight:700;font-size:15px;letter-spacing:.3px;border-radius:3px}
.flame{width:12px;height:16px}
.rule{position:absolute;height:4px;width:50px;background:linear-gradient(90deg,var(--ember),var(--ember-2))}
.section-title{position:absolute;left:0;width:1200px;text-align:center;font-weight:700;font-size:43px;color:#333;letter-spacing:.5px}
.photo{position:absolute}

/* nav */
.brand{position:absolute;display:flex;align-items:center;gap:10px;font-family:"Libre Baskerville",serif;font-weight:700;font-size:30px;color:#2b2b2b}
.brand .dot{width:22px;height:22px;border-radius:50%;background:var(--ember)}
.nav a{position:absolute;top:36px;font-size:12px;font-weight:700;color:#222;text-decoration:none}
.nav a.active{color:var(--ember)}

/* story */
.story-card{position:absolute;left:626px;top:757px;width:520px;height:423px;background:#fff}
.story-card h2{position:absolute;left:60px;top:40px;font-size:43px;font-weight:400;color:#333}
.story-card p{position:absolute;left:60px;width:395px;font-size:14px;line-height:24px;color:var(--muted)}
.text-link{position:absolute;display:flex;align-items:center;gap:7px;color:var(--ember);font-weight:700;font-size:14px}

/* gallery */
.thumb{position:absolute;background:#fff;box-shadow:0 2px 6px rgba(0,0,0,.08)}
.thumb .ph{position:absolute;inset:12px;border-radius:2px}
.arrow{position:absolute;width:42px;height:42px;border-radius:50%;display:flex;align-items:center;justify-content:center}

/* features */
.feat{position:absolute;width:78px;height:78px;border-radius:50%;background:radial-gradient(circle,#3a3a3a,#121212 70%);border:4px solid #fff;box-shadow:0 2px 8px rgba(0,0,0,.25)}
.feat-text{position:absolute;font-size:17px;line-height:24px;color:var(--sand-text)}

/* testimonials */
.review{position:absolute;top:3011px;width:296px;height:210px;background:#fff;box-shadow:0 3px 14px rgba(0,0,0,.08)}
.review .avatar{position:absolute;left:36px;top:18px;width:36px;height:36px;border-radius:50%;background:linear-gradient(#d9c4b4,#9c7f6b)}
.review .name{position:absolute;left:84px;top:22px;font-size:12px;font-weight:700;color:#222}
.review .stars{position:absolute;left:84px;top:38px;font-size:9px;color:#e9a52a}
.review .stars b{color:var(--ember);margin-right:4px}
.review p{position:absolute;left:34px;top:68px;width:230px;font-size:10.5px;line-height:15px;color:#777}
.review .meta{position:absolute;left:34px;top:150px;font-size:9.5px;color:#bbb}
.review .likes{position:absolute;left:34px;top:180px;font-size:9.5px;color:#bbb;display:flex;gap:46px}
.review .likes span:first-child{color:#e9a52a}

/* contact */
.contact-bg{position:absolute;left:0;top:3342px;width:1200px;height:484px;background:linear-gradient(135deg,#3b2d26,#1e1916 55%,#2a221d)}
.contact-line{position:absolute;left:136px;display:flex;align-items:flex-start;gap:10px;color:#eee;font-size:13px;line-height:16px}
.field{position:absolute;background:#fff;border:1px solid #ddd;font-size:11px;color:#777;padding:11px 14px}

/* footer */
.footer{position:absolute;left:0;top:3826px;width:1200px;height:341px;background:var(--night-2)}
.foot-h{position:absolute;top:74px;font-size:11.5px;font-weight:700;color:#fff;letter-spacing:.2px}
.foot-l{position:absolute;font-size:13px;color:#ddd}
.social{position:absolute;top:111px;width:18px;height:18px;border-radius:50%;background:var(--ember)}
</style>
</head>
<body>

<!-- navigation -->
<header>
  <div class="brand" style="left:133px;top:30px"><span class="dot"></span>FIORENZO</div>
  <nav class="nav">
    <a class="active" style="left:569px">HOME</a>
    <a style="left:653px">OUR STORY</a>
    <a style="left:753px">REWIEWS</a>
    <a style="left:841px">GALLERY</a>
  </nav>
  <div class="btn" style="left:923px;top:23px;width:143px;height:43px">CONTACT
    <svg class="flame" viewBox="0 0 12 16"><path d="M6 0C7 4 11 6 11 10.5A5 5 0 0 1 1 10.5C1 8 3 7 3.5 5 5 7 6 4 6 0Z" fill="#fff"/></svg>
  </div>
</header>

<!-- hero -->
<section>
  <div class="photo" role="img" aria-label="Blurred forest park backdrop for the hero" style="left:0;top:84px;width:1200px;height:547px;background:linear-gradient(90deg,#3d4a2a,#5b6a3a 40%,#6d6e4b 70%,#8a8a72)"></div>
  <div class="photo" role="img" aria-label="Black ceramic kamado grill with open lid on a stand, framed by a large flame shape" style="left:650px;top:92px;width:360px;height:530px;border-radius:180px 180px 40px 40px;background:radial-gradient(ellipse at 50% 60%,#2b2b2b 30%,#8a3a1d 60%,rgba(160,60,25,.6) 75%,transparent 76%)"></div>
  <h1 class="abs serif" style="left:139px;top:283px;font-size:56px;line-height:68px;color:#fff;letter-spacing:1px">GRILL TO SUIT<br>YOUR NEEDS</h1>
  <div class="btn" style="left:142px;top:453px;width:168px;height:42px">LEARN MORE
    <svg class="flame" viewBox="0 0 12 16"><path d="M6 0C7 4 11 6 11 10.5A5 5 0 0 1 1 10.5C1 8 3 7 3.5 5 5 7 6 4 6 0Z" fill="#fff"/></svg>
  </div>
</section>

<!-- our story -->
<section>
  <div class="photo" role="img" aria-label="Hand turning meat with tongs over a flaming charcoal grill" style="left:0;top:708px;width:684px;height:485px;background:radial-gradient(ellipse at 45% 65%,#e08a2a,#7a3a12 40%,#2a1a10 80%)"></div>
  <div class="story-card">
    <h2>OUR STORY</h2>
    <div class="rule" style="left:60px;top:106px"></div>
    <p style="top:128px">Lorem ipsum dolor sit amet consectetur. Consectetur neque vitae gravida tempus suspendisse feugiatPorttitor consequat tempor nullam egestas curabitur faucibus amet commodo nulla.</p>
    <p style="top:232px">Morbi mauris tempus imperdiet vivamus condimentum varius pellentesque tincidunt urna.</p>
    <div class="text-link" style="left:64px;top:306px">LEARN MORE
      <svg class="flame" viewBox="0 0 12 16"><path d="M6 0C7 4 11 6 11 10.5A5 5 0 0 1 1 10.5C1 8 3 7 3.5 5 5 7 6 4 6 0Z" fill="var(--ember)"/></svg>
    </div>
  </div>
</section>

<!-- product gallery -->
<section>
  <div class="abs" style="left:0;top:1279px;width:1200px;height:711px;background:var(--soft)"></div>
  <h2 class="section-title" style="top:1350px">PRODUCT GALLERY</h2>
  <div class="rule" style="left:575px;top:1414px"></div>

  <div class="arrow" style="left:73px;top:1622px;background:#9a9a9a">
    <svg width="16" height="14" viewBox="0 0 16 14"><path d="M15 7H2M7 1 1 7l6 6" stroke="#fff" stroke-width="2.6" fill="none"/></svg></div>
  <div class="arrow" style="left:1088px;top:1622px;background:var(--ember)">
    <svg width="16" height="14" viewBox="0 0 16 14"><path d="M1 7h13M9 1l6 6-6 6" stroke="#fff" stroke-width="2.6" fill="none"/></svg></div>

  <div class="thumb" style="left:134px;top:1462px;width:165px;height:171px"><div class="ph" role="img" aria-label="Stainless steel grill spatula" style="background:linear-gradient(135deg,#fff,#cfd3d8 50%,#fff)"></div></div>
  <div class="thumb" style="left:319px;top:1462px;width:165px;height:171px"><div class="ph" role="img" aria-label="Grill seen from the front with open lid" style="background:radial-gradient(circle,#d9d2c3 25%,#333 45%,#fff 62%)"></div></div>
  <div class="thumb" style="left:134px;top:1656px;width:165px;height:171px"><div class="ph" role="img" aria-label="Set of tongs, fork and spatula" style="background:linear-gradient(90deg,#fff,#9aa0a6 30%,#fff 45%,#9aa0a6 60%,#fff)"></div></div>
  <div class="thumb" style="left:319px;top:1656px;width:165px;height:171px"><div class="ph" role="img" aria-label="Aluminium tool carrying case" style="background:linear-gradient(#fff 30%,#b5b9be 40%,#8d9297 65%,#fff 72%)"></div></div>
  <div class="thumb" style="left:503px;top:1462px;width:362px;height:365px"><div class="ph" role="img" aria-label="Black ceramic kamado grill on a stand" style="background:radial-gradient(ellipse at 50% 42%,#2a2a2a 32%,#fff 48%)"></div></div>
  <div class="thumb" style="left:885px;top:1462px;width:181px;height:365px"><div class="ph" role="img" aria-label="Long grilling fork with black handle" style="background:linear-gradient(90deg,#fff 44%,#9aa0a6 48%,#222 52%,#fff 56%)"></div></div>

  <div class="abs" style="left:506px;top:1885px;width:186px;height:43px;border:1.5px solid var(--ember);border-radius:3px;background:#fff;display:flex;align-items:center;justify-content:center;gap:8px;color:var(--ember);font-weight:700;font-size:14px">ALL IN GALLERY
    <svg class="flame" viewBox="0 0 12 16"><path d="M6 0C7 4 11 6 11 10.5A5 5 0 0 1 1 10.5C1 8 3 7 3.5 5 5 7 6 4 6 0Z" fill="var(--ember)"/></svg>
  </div>
</section>

<!-- what will you get -->
<section>
  <div class="abs" style="left:0;top:1990px;width:1200px;height:822px;background:linear-gradient(90deg,#f0e3cc,var(--sand) 50%,#e6d1af)"></div>
  <h2 class="section-title" style="top:2072px">WHAT WILL YOU GET?</h2>
  <div class="rule" style="left:575px;top:2134px"></div>

  <svg class="abs" style="left:0;top:0" width="1200" height="4167" aria-hidden="true">
    <g stroke="#cfb48d" stroke-width="1.2" stroke-dasharray="4 4" fill="none">
      <path d="M406 2243H580"/><path d="M354 2390H520"/><path d="M411 2539H520"/>
      <path d="M794 2244H620"/><path d="M844 2390H700"/><path d="M790 2539H700"/>
    </g>
  </svg>
  <div class="photo" role="img" aria-label="Kamado grill with numbered feature points" style="left:485px;top:2183px;width:227px;height:420px;border-radius:110px 110px 30px 30px;background:radial-gradient(ellipse at 50% 45%,#2b2b2b 50%,transparent 51%)"></div>

  <div class="feat" style="left:328px;top:2204px"></div>
  <div class="feat-text" style="right:890px;top:2218px;text-align:right">Adjustable top damper<br>maintains airflow</div>
  <div class="feat" style="left:276px;top:2351px"></div>
  <div class="feat-text" style="right:941px;top:2380px;text-align:right">Heat insulation handle</div>
  <div class="feat" style="left:333px;top:2500px"></div>
  <div class="feat-text" style="right:885px;top:2510px;text-align:right">Bottom damper to control<br>airflow for precise<br>temperature control</div>

  <div class="feat" style="left:794px;top:2205px"></div>
  <div class="feat-text" style="left:889px;top:2210px">You can see how the<br>temperature changes from<br>the thermometer</div>
  <div class="feat" style="left:844px;top:2351px"></div>
  <div class="feat-text" style="left:939px;top:2366px">Premium hinge<br>Material - Iron</div>
  <div class="feat" style="left:790px;top:2500px"></div>
  <div class="feat-text" style="left:889px;top:2515px">Stripes designed to<br>increase beauty</div>

  <div class="feat" style="left:559px;top:2600px;background:#fff"></div>
  <div class="feat-text" style="left:0;width:1200px;top:2695px;text-align:center">Stainless steel mobile cart<br>with locking casters</div>
</section>

<!-- testimonials -->
<section>
  <h2 class="section-title" style="top:2906px">TESTIMONIALS</h2>
  <div class="rule" style="left:575px;top:2967px"></div>

  <article class="review" style="left:134px">
    <div class="avatar"></div><div class="name">DALE MERCER</div>
    <div class="stars"><b>5.0</b>★★★★★</div>
    <p>"Lorem ipsum dolor sit amet consectetur. Id tortor lectus volutpat aliquam orci at in. In in cras in et. Orci non sit sed amet euismod nulla facilisi pharetra eget."</p>
    <div class="meta">April 02nd, 2022 | Maple Grove, MN</div>
    <div class="likes"><span>👍 12</span><span>👎 00</span></div>
  </article>
  <article class="review" style="left:451px">
    <div class="avatar"></div><div class="name">DALE MERCER</div>
    <div class="stars"><b>5.0</b>★★★★★</div>
    <p>"Lorem ipsum dolor sit amet consectetur. Id tortor lectus volutpat aliquam orci at in. In in cras in et. Orci non sit sed amet euismod nulla facilisi pharetra eget."</p>
    <div class="meta">April 02nd, 2022 | Maple Grove, MN</div>
    <div class="likes"><span>👍 12</span><span>👎 00</span></div>
  </article>
  <article class="review" style="left:768px">
    <div class="avatar"></div><div class="name">DALE MERCER</div>
    <div class="stars"><b>5.0</b>★★★★★</div>
    <p>"Lorem ipsum dolor sit amet consectetur. Id tortor lectus volutpat aliquam orci at in. In in cras in et. Orci non sit sed amet euismod nulla facilisi pharetra eget."</p>
    <div class="meta">April 02nd, 2022 | Maple Grove, MN</div>
    <div class="likes"><span>👍 12</span><span>👎 00</span></div>
  </article>

  <div class="abs" style="left:0;width:1200px;top:3262px;text-align:center;font-size:13px;font-weight:700;color:var(--ember)">READ MORE REVIEWS ON <span style="font-size:20px;color:#4a4a4a">Reviewly</span></div>
</section>

<!-- contact -->
<section>
  <div class="contact-bg" role="img" aria-label="Skewers of grilled vegetables over a barbecue, darkened"></div>
  <h2 class="abs" style="left:129px;top:3470px;font-size:42px;font-weight:700;color:#fff;letter-spacing:2px">CONTACT US</h2>
  <div class="abs" style="left:134px;top:3532px;font-size:15px;font-weight:700;color:#fff">If Any Querry Contact With Us</div>
  <div class="rule" style="left:134px;top:3570px"></div>

  <div class="contact-line" style="top:3610px">
    <svg width="13" height="16" viewBox="0 0 13 16"><path d="M6.5 0A6 6 0 0 0 .5 6c0 4.5 6 10 6 10s6-5.5 6-10a6 6 0 0 0-6-6Zm0 8.5a2.5 2.5 0 1 1 0-5 2.5 2.5 0 0 1 0 5Z" fill="#fff"/></svg>
    <span>2218 Ember Lane, Cedar Falls, Ohio<br>40512</span></div>
  <div class="contact-line" style="top:3658px">
    <svg width="13" height="13" viewBox="0 0 13 13"><path d="M3 .5 5 3.5 3.8 5a7 7 0 0 0 4.2 4.2L9.5 8l3 2-1 2.5C6 13 0 7 .5 1.5Z" fill="#fff"/></svg>
    <span>(305) 555-0148</span></div>
  <div class="contact-line" style="top:3692px">
    <svg width="13" height="10" viewBox="0 0 13 10"><rect width="13" height="10" fill="#fff"/><path d="M0 0 6.5 5.5 13 0" stroke="#333" fill="none"/></svg>
    <span>fiorenzo.info@mail.com</span></div>

  <div class="field" style="left:577px;top:3468px;width:228px;height:41px">Name</div>
  <div class="field" style="left:834px;top:3468px;width:230px;height:41px">Phone number</div>
  <div class="field" style="left:577px;top:3528px;width:487px;height:39px">Email Address</div>
  <div class="field" style="left:577px;top:3588px;width:487px;height:102px">Message</div>
  <div class="btn" style="left:577px;top:3719px;width:134px;height:44px">SEND US
    <svg class="flame" viewBox="0 0 12 16"><path d="M6 0C7 4 11 6 11 10.5A5 5 0 0 1 1 10.5C1 8 3 7 3.5 5 5 7 6 4 6 0Z" fill="#fff"/></svg>
  </div>
</section>

<!-- footer -->
<footer class="footer">
  <div class="brand" style="left:136px;top:68px;color:#fff"><span class="dot"></span>FIORENZO</div>

  <div class="foot-h" style="left:495px">PAGE SECTION LINKS</div>
  <div class="foot-l" style="left:495px;top:115px">Home</div>
  <div class="foot-l" style="left:495px;top:144px">Our Story</div>
  <div class="foot-l" style="left:495px;top:173px">Rewiews</div>
  <div class="foot-l" style="left:495px;top:202px">FAQ</div>

  <div class="foot-h" style="left:686px">CONTACT &amp; SUPPORT</div>
  <div class="foot-l" style="left:686px;top:115px">Delivery &amp; Returns</div>
  <div class="foot-l" style="left:686px;top:144px">Customer Care</div>
  <div class="foot-l" style="left:686px;top:173px">Contact</div>

  <div class="foot-h" style="left:896px">FOLLOW OUR SOCIA MEDIA</div>
  <div class="social" style="left:898px"></div>
  <div class="social" style="left:950px"></div>
  <div class="social" style="left:1002px"></div>

  <div class="abs" style="left:136px;top:260px;width:930px;height:1px;background:#3a302c"></div>
  <div class="foot-l" style="left:136px;top:280px;font-size:12.5px">©2023 FIORENZO. All rights reserved.</div>
  <div class="foot-l" style="left:822px;top:282px;font-size:12.5px">Privacy Policy &nbsp; | &nbsp; Terms And Conditions</div>
</footer>

</body>
</html>
```